Business Card design for construction company

I would like a business card design for a construction company - Harlow Constructions. I have attached the ai logo file for use. I would like the card to be very smart and clean and incorporate only white and the two colours in the logo. I would like the card to have two sides. One side can just have the logo, the other with the relevant information.

Target Market(s)

Building and Construction Clients

Industry/Entity Type

Business

Contact Information for Business Card

Name: Tom Pardoe
Company: Harlow Constructions Pty Limited
Address: 14 Mallee Crescent Carrow Vale 2093
Phone: 0427 531 068
Email: tomp@harlowbuild-example.com.au

Font styles to use
Serif
Sans Serif

Requirements
Must have
• Details noted above
• Logo as provided
• Colours as in logo
• Square edges
• A font that compliments the logo
Should not have
• Any colour other than white and those in logo
• Rounded edges

```html
<!DOCTYPE html>
<html lang="en">
<head>
<meta charset="utf-8">
<title>Harlow Constructions – Business Card</title>
<link rel="stylesheet" href="https://fonts.googleapis.com/css2?family=Noto+Serif&family=Open+Sans:wght@400&display=swap">
<style>
  :root {
    --backdrop: #5a5b5d;
    --card: #ffffff;
    --brand-blue: #00adef;
    --brand-grey: #4d4d4f;
    --map-tint: #f1f1f2;
    --map-dots: #f5f5f6;
    --ink-light: #ffffff;
  }
  * { margin: 0; padding: 0; box-sizing: border-box; }
  html, body {
    width: 1200px; height: 1200px; overflow: hidden;
    background: var(--backdrop);
    font-family: "Open Sans", Arial, sans-serif;
  }
  .card {
    position: absolute; left: 200px; width: 800px; height: 476px;
    background: var(--card); overflow: hidden;
  }
  .card--front { top: 80px; }
  .card--back { top: 644px; }

  .front-shapes { position: absolute; inset: 0; width: 800px; height: 476px; }

  .map-area { position: absolute; }
  .card--front .map-area {
    left: 0; top: 72px; width: 470px; height: 330px;
    background: radial-gradient(ellipse at 45% 45%, var(--map-tint) 55%, rgba(241,241,242,0) 75%);
  }
  .card--back .map-area {
    left: 52px; top: 64px; width: 696px; height: 348px;
    background: radial-gradient(ellipse at 50% 45%, var(--map-dots) 55%, rgba(245,245,246,0) 75%);
  }

  .wordmark {
    position: absolute; display: flex; align-items: center;
    color: var(--brand-grey); font-weight: 400;
    text-transform: uppercase; white-space: nowrap;
  }
  .wordmark__square { background: var(--brand-blue); flex: none; }
  .card--front .wordmark { left: 52px; top: 222px; font-size: 21px; letter-spacing: 2.5px; gap: 12px; }
  .card--front .wordmark__square { width: 10px; height: 10px; }
  .card--back .wordmark { left: 0; right: 0; justify-content: center; top: 434px; top: 436px; }
  .card--back .wordmark { top: 208px; font-size: 36px; letter-spacing: 4px; gap: 18px; }
  .card--back .wordmark__square { width: 16px; height: 16px; }

  .holder-name {
    position: absolute; right: 36px; top: 44px;
    font-family: "Noto Serif", Georgia, serif; font-size: 34px;
    color: var(--ink-light); font-weight: 400;
  }
  .contact-list { position: absolute; right: 36px; top: 278px; list-style: none; }
  .contact-item {
    display: flex; justify-content: flex-end; align-items: center;
    height: 39px; gap: 14px;
    color: var(--ink-light); font-size: 15px; letter-spacing: 0.4px;
  }
  .contact-icon { width: 24px; height: 24px; flex: none; }
</style>
</head>
<body>

<section class="card card--front" aria-label="Front of card">
  <div class="map-area" role="img" aria-label="Faint world map background"></div>

  <svg class="front-shapes" viewBox="0 0 1000 595" preserveAspectRatio="none" aria-hidden="true">
    <path fill="var(--brand-grey)" d="M572 27 H606 C610 300 530 470 385 595 H368 C510 470 578 300 572 27 Z"/>
    <path fill="none" stroke="var(--card)" stroke-width="6" d="M606 0 C610 300 530 470 385 595"/>
    <path fill="var(--brand-blue)" d="M609 0 H1000 V595 H390 C535 470 613 300 609 0 Z"/>
  </svg>

  <div class="wordmark"><span class="wordmark__square"></span>Harlow Constructions</div>

  <h1 class="holder-name">Tom Pardoe</h1>

  <ul class="contact-list">
    <li class="contact-item">0427 531 068
      <svg class="contact-icon" viewBox="0 0 24 24" aria-hidden="true"><path fill="#fff" d="M6.6 2.5c.5-.3 1.1-.2 1.4.3l2.2 3.4c.3.5.2 1.1-.2 1.4L8.6 8.8c1 2.4 3 4.5 5.4 5.6l1.2-1.4c.4-.4 1-.5 1.4-.2l3.4 2.1c.5.3.6.9.3 1.4l-1.4 2.4c-.5.8-1.5 1.2-2.4.9C9.7 18 5.7 13.9 4.4 7.1c-.2-.9.2-1.9 1-2.4z"/></svg>
    </li>
    <li class="contact-item">tomp@harlowbuild-example.com.au
      <svg class="contact-icon" viewBox="0 0 24 24" aria-hidden="true"><g fill="none" stroke="#fff" stroke-width="1.6"><rect x="2" y="5" width="20" height="14"/><path d="M2 5l10 8 10-8M2 19l7.5-7M22 19l-7.5-7"/></g></svg>
    </li>
    <li class="contact-item">Harlow Constructions Pty Limited
      <svg class="contact-icon" viewBox="0 0 24 24" aria-hidden="true"><g fill="none" stroke="#fff" stroke-width="1.3"><path d="M7 22V5h10v17M10 5V2h4v3M3 22h18"/><path d="M9.5 8h1M13.5 8h1M9.5 11h1M13.5 11h1M9.5 14h1M13.5 14h1M9.5 17h1M13.5 17h1"/></g></svg>
    </li>
    <li class="contact-item">14 Mallee Crescent Carrow Vale 2093
      <svg class="contact-icon" viewBox="0 0 24 24" aria-hidden="true"><path fill="#fff" fill-rule="evenodd" d="M12 1.5a7.5 7.5 0 0 1 7.5 7.5c0 5.2-7.5 13.5-7.5 13.5S4.5 14.2 4.5 9A7.5 7.5 0 0 1 12 1.5zm0 4.3a3.2 3.2 0 1 0 0 6.4 3.2 3.2 0 0 0 0-6.4z"/></svg>
    </li>
  </ul>
</section>

<section class="card card--back" aria-label="Back of card">
  <div class="map-area" role="img" aria-label="Faint dotted world map background"></div>
  <div class="wordmark"><span class="wordmark__square"></span>Harlow Constructions</div>
</section>

</body>
</html>
```